Website Refresh Needed - Large Couples Therapy Group

We are a large couples counselling group in Australia, and we have some key pages of our website that need refreshing, as it's a few years old now.
Similar colour palette as currently, and the same colours as the logo. No new logo required.
Total of 7 new (updated) page templates designs are needed:
1. HOME: https://www.velmoraclinic.com.au/
2: CONTACT US: https://www.velmoraclinic.com.au/contact/
3: RC CITY PAGE: https://www.velmoraclinic.com.au/city/sydney/
4: ST CITY PAGE: https://www.velmoraclinic.com.au/our-counselling/sex-therapy/sex-therapy-sydney/
5: ALL BLOGS: https://www.velmoraclinic.com.au/blog/
6: BLOG: https://www.velmoraclinic.com.au/sexual-desires-in-men-and-women-what-are-the-real-differences/
7: MAIN STANDARD PAGE: https://www.velmoraclinic.com.au/our-counselling/couples-relationship-counselling/

Target Market(s)

couples who are going through a crisis in their relationship or marriage.

Number of Pages Required

5+ page

Colors
86cfc6
b8a6cd
cfdfed

Requirements
Must have
• Calm, reassuring colours. People are stressed and need to know we can help.
Should not have
• No bright oranges or yellows.

```html
<!DOCTYPE html>
<html lang="en">
<head>
<meta charset="utf-8">
<title>Velmora Clinic – Helping You Create Loving Relationships</title>
<link href="https://fonts.googleapis.com/css2?family=Quicksand:wght@400;500;600;700&family=Lato:wght@400;700&display=swap" rel="stylesheet">
<style>
:root{
  --teal:#86cfc6;
  --teal-dark:#5fb8ad;
  --purple:#b8a6cd;
  --purple-text:#a994c4;
  --ice:#cfdfed;
  --ink:#2f2f2f;
  --body:#6b6b6b;
  --soft-bg:#eef3f4;
  --footer:#6c6c6c;
  --white:#ffffff;
}
*{box-sizing:border-box;margin:0;padding:0}
html,body{width:1200px;height:4045px;overflow:hidden;background:var(--white)}
body{position:relative;font-family:'Lato',sans-serif;color:var(--body)}
.abs{position:absolute}
.heading{font-family:'Quicksand',sans-serif;font-weight:500;color:var(--ink);letter-spacing:.5px}
.btn{position:absolute;display:flex;align-items:center;justify-content:center;background:var(--purple);color:var(--white);font-family:'Quicksand',sans-serif;font-weight:500;font-size:18px;letter-spacing:.5px}
.photo{position:absolute}

/* header */
.site-header{position:absolute;left:0;top:0;width:1200px;height:96px;background:var(--white)}
.brand{position:absolute;left:110px;top:26px;display:flex;align-items:center;gap:12px}
.brand-mark{width:40px;height:40px;border-radius:50%;background:var(--teal)}
.brand-name{font-family:'Quicksand',sans-serif;font-weight:600;font-size:32px;color:var(--teal-dark)}
.call{position:absolute;left:552px;top:30px;display:flex;align-items:center;gap:10px;font-family:'Quicksand',sans-serif;font-size:16px;color:#444}
.call b{font-weight:700;margin-left:6px}
.icon-ring{width:36px;height:36px;border-radius:50%;border:1.5px solid #aaa;display:flex;align-items:center;justify-content:center}
.main-nav{position:absolute;left:0;top:96px;width:1200px;height:41px;border-top:1px solid #e3e3e3;border-bottom:1px solid #e3e3e3}
.main-nav span{position:absolute;top:11px;font-family:'Quicksand',sans-serif;font-size:16px;color:#333;font-weight:500}
.main-nav .current{color:var(--purple-text)}

/* hero */
.hero{position:absolute;left:0;top:137px;width:1200px;height:490px;background:linear-gradient(100deg,#b9aea6 0%,#cfc4ba 35%,#b89a84 60%,#8a7a72 100%)}
.hero-title{position:absolute;left:108px;top:62px;font-family:'Quicksand',sans-serif;font-weight:500;font-size:64px;line-height:76px;color:var(--white)}
.hero-btn{position:absolute;left:108px;top:318px;width:205px;height:60px;border:2px solid var(--white);color:var(--white);display:flex;align-items:center;justify-content:center;font-family:'Quicksand',sans-serif;font-size:18px;font-weight:500}
.dots{position:absolute;left:566px;top:425px;display:flex;gap:6px}
.dots i{width:13px;height:13px;border-radius:50%;border:2px solid var(--white)}
.dots i:first-child{background:var(--white)}

/* search */
.search{position:absolute;left:0;top:627px;width:1200px;height:136px;background:var(--teal)}
.search h2{position:absolute;left:0;width:1200px;top:21px;text-align:center;font-family:'Quicksand',sans-serif;font-weight:500;font-size:26px;color:var(--white)}
.field{position:absolute;top:68px;height:42px;background:var(--white);border:1px solid #ddd;font-size:15px;color:#777;padding:12px 16px}

/* welcome */
.welcome-title{left:576px;top:810px;font-size:48px;line-height:60px}
.welcome-text{position:absolute;left:576px;width:515px;font-size:14.5px;line-height:29px;color:var(--body)}

/* services */
.services{position:absolute;left:0;top:1316px;width:1200px;height:579px;background:var(--soft-bg)}
.section-title{position:absolute;left:0;width:1200px;text-align:center;font-size:48px}
.service{position:absolute;top:144px;width:250px;text-align:center}
.service .ring{width:172px;height:172px;margin:0 auto;border:2px solid var(--teal);border-radius:50%;display:flex;align-items:center;justify-content:center}
.service .ring-fill{width:96px;height:96px;border-radius:50%;background:linear-gradient(135deg,#ece6f3,#dcd2e8)}
.service h3{margin-top:18px;font-family:'Quicksand',sans-serif;font-weight:500;font-size:23px;line-height:33px;color:#444}
.service p{margin:10px auto 0;width:250px;font-size:14px;line-height:28px;color:var(--body)}
.service .more{margin-top:12px;font-family:'Quicksand',sans-serif;font-size:15px;color:var(--purple-text);font-weight:500}

/* therapists */
.issue-list{position:absolute;list-style:none;font-size:15px;color:#555}
.issue-list li{position:relative;padding-left:28px;line-height:20px}
.issue-list li svg{position:absolute;left:0;top:3px}

/* quote */
.quote{position:absolute;left:0;top:2502px;width:1200px;height:321px;background:linear-gradient(90deg,#b4a2cb,#bca9d1 50%,#c1b3d4)}
.quote p{position:absolute;left:150px;width:900px;top:55px;text-align:center;font-family:'Quicksand',sans-serif;font-size:27px;line-height:46px;color:var(--white)}
.quote .author{position:absolute;left:0;width:1200px;top:222px;text-align:center;font-family:'Quicksand',sans-serif;font-weight:700;font-size:24px;color:var(--white);letter-spacing:1px}

/* blog */
.post{position:absolute;top:2968px;width:312px}
.post .photo{position:relative;width:312px;height:217px}
.post .date{position:absolute;left:0;bottom:0;width:64px;height:62px;background:var(--teal);color:var(--white);font-family:'Quicksand',sans-serif;font-weight:600;font-size:16px;line-height:23px;padding:9px 7px}
.post h3{margin-top:20px;font-family:'Quicksand',sans-serif;font-weight:500;font-size:20px;line-height:31px;color:#222}

/* contact */
.contact{position:absolute;left:0;top:3450px;width:1200px;height:595px;background:var(--footer)}
.contact h4{position:absolute;font-family:'Quicksand',sans-serif;font-weight:600;font-size:22px;color:var(--white)}
.input{position:absolute;background:var(--white);border:1px solid #ccc;border-radius:3px;font-size:15px;color:#666;padding:12px 16px}
.info-row{position:absolute;left:778px;display:flex;align-items:center;gap:18px;color:var(--white);font-size:16px}
.info-row .icon-ring{border-color:#ddd}
.social{position:absolute;top:3812px;width:34px;height:34px;border-radius:50%;border:1.5px solid #ddd}
.rule{position:absolute;left:108px;top:3975px;width:980px;height:1px;background:#8a8a8a}
.copyright{position:absolute;left:0;width:1200px;top:4000px;text-align:center;font-size:16px;color:var(--white)}
</style>
</head>
<body>

<header class="site-header">
  <div class="brand"><span class="brand-mark"></span><span class="brand-name">Velmora Clinic</span></div>
  <div class="call">
    <span class="icon-ring"><svg width="16" height="16" viewBox="0 0 24 24"><path d="M6.6 10.8a15.1 15.1 0 0 0 6.6 6.6l2.2-2.2a1 1 0 0 1 1-.25 11.4 11.4 0 0 0 3.6.57 1 1 0 0 1 1 1V20a1 1 0 0 1-1 1A17 17 0 0 1 3 4a1 1 0 0 1 1-1h3.5a1 1 0 0 1 1 1c0 1.25.2 2.45.57 3.57a1 1 0 0 1-.25 1z" fill="#999"/></svg></span>
    <span>Call Us Now<b>1300 555 019</b></span>
  </div>
  <div class="btn" style="left:835px;top:22px;width:253px;height:52px;font-size:16px">REQUEST AN APPOINTMENT</div>
</header>

<nav class="main-nav">
  <span class="current" style="left:118px">Home</span>
  <span style="left:203px">Counselling Types</span>
  <span style="left:385px">Relationship Counselling Locations</span>
  <span style="left:699px">Sex Therapy Locations</span>
  <span style="left:920px">Blog</span>
  <span style="left:993px">Contact Us</span>
</nav>

<section class="hero">
  <div class="photo" role="img" aria-label="Photo of a couple embracing forehead to forehead by the sea at sunset" style="left:0;top:0;width:1200px;height:490px;background:linear-gradient(100deg,rgba(0,0,0,0) 40%,rgba(120,90,70,.35) 100%)"></div>
  <h1 class="hero-title">Helping You<br>Create Loving<br>Relationships</h1>
  <div class="hero-btn">GET MORE INFO</div>
  <div class="dots"><i></i><i></i><i></i><i></i></div>
</section>

<section class="search">
  <h2>SEARCH OUR THERAPISTS NEAR YOU</h2>
  <div class="field" style="left:110px;width:268px">Type of Counselling
    <svg class="abs" style="right:14px;top:16px" width="12" height="8" viewBox="0 0 12 8"><path d="M1 1l5 5 5-5" fill="none" stroke="#888" stroke-width="1.5"/></svg>
  </div>
  <div class="field" style="left:388px;width:268px">Location</div>
  <div class="field" style="left:666px;width:268px">Zipcode</div>
  <div class="btn" style="left:946px;top:59px;width:142px;height:52px;font-size:19px">SEARCH</div>
</section>

<section class="welcome">
  <div class="photo" role="img" aria-label="Photo of two hands joined into a heart shape" style="left:108px;top:785px;width:392px;height:465px;border-radius:50% 50% 46% 54% / 48% 48% 52% 52%;background:linear-gradient(135deg,#c9a594 0%,#8f8c86 50%,#5f7a80 100%)"></div>
  <h2 class="heading abs welcome-title">WELCOME TO<br>VELMORA CLINIC</h2>
  <p class="welcome-text" style="top:940px">Our vision is to be the most highly regarded and comprehensive marriage counselling, relationship counselling and sex therapy service in Australia, at reasonable and affordable rates.</p>
  <p class="welcome-text" style="top:1057px">We hand choose our team of Registered Psychologists, Counsellors and Sex Therapists considering their knowledge, compassion, and unbiased approach to marriage counselling and sexual therapy and their experience in the relationship field.</p>
  <div class="btn" style="left:576px;top:1202px;width:156px;height:54px">READ MORE</div>
</section>

<section class="services">
  <h2 class="heading section-title" style="top:55px">OUR SERVICES</h2>
  <div class="service" style="left:87px">
    <div class="ring"><div class="ring-fill" role="img" aria-label="Line illustration of a couple with a heart"></div></div>
    <h3>Relationship<br>Counselling</h3>
    <p>We take a positive approach when helping you with your relationship problems</p>
    <div class="more">READ MORE</div>
  </div>
  <div class="service" style="left:345px">
    <div class="ring"><div class="ring-fill" role="img" aria-label="Line illustration of linked gender symbols"></div></div>
    <h3>Sex Therapy<br>Counselling</h3>
    <p>Sex and lovemaking can be the most delicious or dissatisfying part of your life and your relationship.</p>
    <div class="more">READ MORE</div>
  </div>
  <div class="service" style="left:603px">
    <div class="ring"><div class="ring-fill" role="img" aria-label="Line illustration of a frustrated figure"></div></div>
    <h3>Anger Management<br>Counselling</h3>
    <p>As we have found that a major cause of relationship issues is poor anger management</p>
    <div class="more">READ MORE</div>
  </div>
  <div class="service" style="left:862px">
    <div class="ring"><div class="ring-fill" role="img" aria-label="Line illustration of a self-focused figure"></div></div>
    <h3>Narcissism<br>Counselling</h3>
    <p>An integral part of a healthy relationship is a sense of equality and consideration</p>
    <div class="more">READ MORE</div>
  </div>
</section>

<section class="therapists">
  <h2 class="heading abs" style="left:108px;top:1945px;font-size:48px;line-height:58px">OUR RELATIONSHIP<br>THERAPISTS</h2>
  <ul class="issue-list" style="left:108px;top:2086px">
    <li style="margin-bottom:13px"><svg width="14" height="12" viewBox="0 0 14 12"><path d="M1 6l4 4 8-9" fill="none" stroke="var(--teal)" stroke-width="2.5"/></svg>Affairs</li>
    <li style="margin-bottom:13px"><svg width="14" height="12" viewBox="0 0 14 12"><path d="M1 6l4 4 8-9" fill="none" stroke="var(--teal)" stroke-width="2.5"/></svg>Controlling behaviour</li>
    <li style="margin-bottom:13px"><svg width="14" height="12" viewBox="0 0 14 12"><path d="M1 6l4 4 8-9" fill="none" stroke="var(--teal)" stroke-width="2.5"/></svg>Verbal abuse</li>
    <li style="margin-bottom:13px"><svg width="14" height="12" viewBox="0 0 14 12"><path d="M1 6l4 4 8-9" fill="none" stroke="var(--teal)" stroke-width="2.5"/></svg>Imbalance of power</li>
    <li style="margin-bottom:13px"><svg width="14" height="12" viewBox="0 0 14 12"><path d="M1 6l4 4 8-9" fill="none" stroke="var(--teal)" stroke-width="2.5"/></svg>Lack of intimacy</li>
    <li style="margin-bottom:13px"><svg width="14" height="12" viewBox="0 0 14 12"><path d="M1 6l4 4 8-9" fill="none" stroke="var(--teal)" stroke-width="2.5"/></svg>Poor communication</li>
    <li style="margin-bottom:13px"><svg width="14" height="12" viewBox="0 0 14 12"><path d="M1 6l4 4 8-9" fill="none" stroke="var(--teal)" stroke-width="2.5"/></svg>Loss of love</li>
    <li><svg width="14" height="12" viewBox="0 0 14 12"><path d="M1 6l4 4 8-9" fill="none" stroke="var(--teal)" stroke-width="2.5"/></svg>Relationship neglect</li>
  </ul>
  <ul class="issue-list" style="left:325px;top:2086px">
    <li style="margin-bottom:21px"><svg width="14" height="12" viewBox="0 0 14 12"><path d="M1 6l4 4 8-9" fill="none" stroke="var(--teal)" stroke-width="2.5"/></svg>Sexual problems</li>
    <li style="margin-bottom:21px"><svg width="14" height="12" viewBox="0 0 14 12"><path d="M1 6l4 4 8-9" fill="none" stroke="var(--teal)" stroke-width="2.5"/></svg>Problems from childhood</li>
    <li style="margin-bottom:21px"><svg width="14" height="12" viewBox="0 0 14 12"><path d="M1 6l4 4 8-9" fill="none" stroke="var(--teal)" stroke-width="2.5"/></svg>Problems with parenting<br>your children</li>
    <li style="margin-bottom:21px"><svg width="14" height="12" viewBox="0 0 14 12"><path d="M1 6l4 4 8-9" fill="none" stroke="var(--teal)" stroke-width="2.5"/></svg>Step children and in-laws</li>
    <li style="margin-bottom:21px"><svg width="14" height="12" viewBox="0 0 14 12"><path d="M1 6l4 4 8-9" fill="none" stroke="var(--teal)" stroke-width="2.5"/></svg>All forms of family problems</li>
    <li><svg width="14" height="12" viewBox="0 0 14 12"><path d="M1 6l4 4 8-9" fill="none" stroke="var(--teal)" stroke-width="2.5"/></svg>Anger management problems</li>
  </ul>
  <div class="btn" style="left:108px;top:2382px;width:157px;height:55px">READ MORE</div>
  <div class="abs" style="left:629px;top:1922px;width:530px;height:530px;border-radius:50%;background:var(--teal)"></div>
  <div class="photo" role="img" aria-label="Photo of a smiling therapist listening to a client across a desk" style="left:651px;top:1944px;width:486px;height:486px;border-radius:50%;background:linear-gradient(120deg,#3b3b3d 0%,#6e7f88 45%,#c9ccd0 75%,#e8e6e2 100%)"></div>
</section>

<section class="quote">
  <div class="photo" role="img" aria-label="Faint background photo of a couple, tinted lavender" style="left:0;top:0;width:1200px;height:321px;background:linear-gradient(90deg,rgba(255,255,255,0) 30%,rgba(255,255,255,.12) 100%)"></div>
  <svg class="abs" style="left:92px;top:138px" width="22" height="40" viewBox="0 0 22 40"><path d="M18 3L4 20l14 17" fill="none" stroke="#fff" stroke-width="3"/></svg>
  <svg class="abs" style="left:1086px;top:138px" width="22" height="40" viewBox="0 0 22 40"><path d="M4 3l14 17L4 37" fill="none" stroke="#fff" stroke-width="3"/></svg>
  <p>“ Conection is the energy betwen people when they feel seen, heard, and valued; when they can give and receive without judegement; and when they get sustenance and strength from the relationship. ”</p>
  <div class="author">- MAREN ASTLEY</div>
</section>

<section class="blog">
  <h2 class="heading section-title" style="top:2880px">LATEST BLOG</h2>
  <article class="post" style="left:110px">
    <div class="photo" role="img" aria-label="Photo of a troubled woman with a man in the background" style="background:linear-gradient(120deg,#e9e2d6,#cfd4d8 60%,#b7c3cc)"><div class="date">24,Jun<br>2020</div></div>
    <h3>What is Borderline Personality Disorder and how does it affect my relationship?</h3>
  </article>
  <article class="post" style="left:445px">
    <div class="photo" role="img" aria-label="Photo of a laughing couple under a white sheet" style="background:linear-gradient(120deg,#d9b08a,#c39a7e 50%,#eeeae6)"><div class="date">24,Jun<br>2020</div></div>
    <h3>Sexual Desires in Men and Women; What Are the Real Differences?</h3>
  </article>
  <article class="post" style="left:776px">
    <div class="photo" role="img" aria-label="Photo of a couple lying together on a blanket in dry grass" style="background:linear-gradient(120deg,#d8d4cf,#b59b8c 55%,#9b8a6a)"><div class="date">24,Jun<br>2020</div></div>
    <h3>6 Steps To Becoming An Emotionally Available Lover</h3>
  </article>
  <div class="btn" style="left:522px;top:3333px;width:156px;height:55px">VIEW MORE</div>
</section>

<footer class="contact">
  <h2 class="abs" style="left:0;width:1200px;top:48px;text-align:center;font-family:'Quicksand',sans-serif;font-weight:500;font-size:48px;color:#fff">CONTACT US</h2>
  <h4 style="left:110px;top:137px">Request a Quote</h4>
  <h4 style="left:778px;top:137px">Contact Information</h4>
  <h4 style="left:778px;top:308px">Social Media</h4>
</footer>
<div class="input" style="left:110px;top:3645px;width:298px;height:46px">Name :</div>
<div class="input" style="left:417px;top:3645px;width:297px;height:46px">Phone no :</div>
<div class="input" style="left:110px;top:3707px;width:604px;height:46px">Email :</div>
<div class="input" style="left:110px;top:3768px;width:604px;height:84px">Message :</div>
<div class="btn" style="left:603px;top:3870px;width:111px;height:50px">SUBMIT</div>

<div class="info-row" style="top:3643px">
  <span class="icon-ring"><svg width="15" height="15" viewBox="0 0 24 24"><path d="M6.6 10.8a15.1 15.1 0 0 0 6.6 6.6l2.2-2.2a1 1 0 0 1 1-.25 11.4 11.4 0 0 0 3.6.57 1 1 0 0 1 1 1V20a1 1 0 0 1-1 1A17 17 0 0 1 3 4a1 1 0 0 1 1-1h3.5a1 1 0 0 1 1 1c0 1.25.2 2.45.57 3.57a1 1 0 0 1-.25 1z" fill="#fff"/></svg></span>
  <span>1300 555 019</span>
</div>
<div class="info-row" style="top:3706px">
  <span class="icon-ring"><svg width="15" height="12" viewBox="0 0 15 12"><rect x="0" y="0" width="15" height="12" rx="1.5" fill="#fff"/><path d="M1 1.5l6.5 5 6.5-5" fill="none" stroke="#6c6c6c" stroke-width="1.4"/></svg></span>
  <span>info@velmoraclinic.com.au</span>
</div>
<span class="social" style="left:776px"></span>
<span class="social" style="left:822px"></span>
<span class="social" style="left:868px"></span>

<div class="rule"></div>
<div class="copyright">Copyright © 2020, Velmora Clinic. All rights reserved.</div>
<svg class="abs" style="left:1063px;top:4002px" width="26" height="16" viewBox="0 0 26 16"><path d="M2 14L13 3l11 11" fill="none" stroke="#fff" stroke-width="3"/></svg>

</body>
</html>
```